Business card design for web travel company

Hi
we'd like to receive some proposal for a business card design.
Stayvano is a private travel club, dedicated to all travel lovers, with unique offers for exclusive destinations all around the world. At Stayvano you can find a wide range of offers for resorts, boutique hotels and travel packages at the best guaranteed price available on the market. The convenience of the offer is guaranteed by a private sales model: offers are available for a limited time only and they are personally chosen by Stayvano's qualified team of travel experts.
We offer only exclusive hotels with discounted prices but we are not an outlet or a discount supermarket: the design should reflect our connection with luxury, exclusivity using the same style of our website www.stayvano-example.com.
We want to make sure that when we'll present ourself to our business partner they will feel immediately which is our brand positioning giving them also a sense of an affordable and reliable partner.
In attachment you can also find our brand guidelines (please note that we are NOT USING ANY MORE THE TAG LINE "Five star outlet" mentioned in it).
The info to be inserted are:
Name Surname
Job Title
Tel
Mobile (when needed)
Email
Stayvano S.r.l.
Via Bruno Lesta 27
20131 Milano

```html
<!DOCTYPE html>
<html lang="it">
<head>
<meta charset="utf-8">
<title>Stayvano – Business Card</title>
<link rel="stylesheet" href="https://fonts.googleapis.com/css2?family=Barlow:wght@300;400&display=swap">
<style>
  :root {
    --ink: #000000;
    --paper: #ffffff;
    --gold: #b9aa7c;
    --text: #ffffff;
  }
  * { margin: 0; padding: 0; box-sizing: border-box; }
  html, body {
    width: 1062px;
    height: 1200px;
    overflow: hidden;
    background: var(--paper);
  }
  body {
    position: relative;
    font-family: "Barlow", "DIN Alternate", Arial, sans-serif;
    font-weight: 300;
    color: var(--text);
  }
  .card {
    position: absolute;
    left: 2px;
    width: 1060px;
    background: var(--ink);
  }
  .card--front { top: 0; height: 592px; }
  .card--back { top: 610px; height: 590px; }

  .brand-name {
    position: absolute;
    left: 55px;
    top: 38px;
    font-size: 84px;
    font-weight: 300;
    letter-spacing: 1px;
    line-height: 1;
    color: var(--text);
  }

  .contact {
    position: absolute;
    font-size: 31px;
    line-height: 1;
    white-space: nowrap;
    letter-spacing: 0.8px;
  }
  .contact__person { right: 62px; top: 392px; }
  .contact__address { right: 122px; top: 434px; }
  .contact__phones { right: 62px; top: 476px; }
  .contact__email { right: 102px; top: 513px; color: var(--gold); }
  .accent { color: var(--gold); }

  .tagline {
    position: absolute;
    right: 52px;
    bottom: 44px;
    font-size: 31px;
    line-height: 1;
    letter-spacing: 0.8px;
    color: var(--gold);
    white-space: nowrap;
  }
  .tagline__emphasis { color: var(--text); }
</style>
</head>
<body>
  <section class="card card--front">
    <div class="brand-name">Stayvano</div>
    <p class="contact contact__person"><span class="accent">Marco Rinaldi</span> I General Manager</p>
    <p class="contact contact__address">Stayvano S.r.l., Via Bruno Lesta 27, 20131, Milano</p>
    <p class="contact contact__phones">T: 02 5550 1827 I F: 02 5550 1828</p>
    <p class="contact contact__email">info@stayvano-example.com</p>
  </section>

  <section class="card card--back">
    <p class="tagline">where <span class="tagline__emphasis">every</span> journey feels like coming home</p>
  </section>
</body>
</html>
```